Lets get creative with Pelloway Finance Brochure

I have used artfolkhub before for a previous brochure which is attached business BRAMLE Automotive. I would like to work together on a new project PELLOWAY Finance. https://pellowayfinance.com.au/
It is a boutique Finance company ideally targeting the small to Medium business s along with consumer finance. I have attached previous brochure to give an idea of layout. Once we have a layout i will send wording through.

Target Market(s)

business owners

Industry/Entity Type

Finance

Font styles to use
Serif

Colors
0355a3
fef3ec

```html
<!DOCTYPE html>
<html lang="en">
<head>
<meta charset="utf-8">
<title>Pelloway Finance Brochure</title>
<link rel="stylesheet" href="https://fonts.googleapis.com/css2?family=Montserrat:wght@500;700&family=Rubik:wght@300;400&display=swap">
<style>
  :root {
    --navy: #223a73;
    --sky: #6b9fd8;
    --slate: #7d89a6;
    --charcoal: #3b4048;
    --pink: #f2a5c0;
    --pink-soft: #f6bfd2;
    --map: #a9c3e6;
    --white: #ffffff;
    --ink: #1d1d1d;
    --rule: #2e4272;
  }
  * { margin: 0; padding: 0; box-sizing: border-box; }
  html, body { width: 776px; height: 1200px; overflow: hidden; background: var(--white); }
  .sheet { position: relative; width: 776px; height: 1200px; font-family: "Rubik", sans-serif; color: var(--ink); }
  .abs { position: absolute; }
  .layer { position: absolute; left: 0; }

  .fold { position: absolute; width: 1px; background: var(--rule); opacity: .6; }

  .brand { font-family: "Montserrat", sans-serif; font-weight: 500; color: var(--navy); text-align: center; line-height: 1; }
  .brand .name { display: block; font-size: 26px; letter-spacing: 5px; }
  .brand .sub { display: block; font-size: 10px; letter-spacing: 9px; margin-top: 8px; }

  .photo { position: absolute; }

  .about-title, .why-title { font-family: "Montserrat", sans-serif; font-weight: 700; color: var(--navy); font-size: 18px; }
  .about-text { font-size: 12.5px; font-weight: 300; color: var(--white); line-height: 17px; width: 205px; }
  .why-dots { list-style: none; }
  .why-dots li { width: 5px; height: 5px; border-radius: 50%; background: var(--navy); margin-bottom: 9.5px; }

  .address-title { font-family: "Montserrat", sans-serif; font-weight: 500; color: var(--sky); font-size: 20px; letter-spacing: 1px; width: 255px; text-align: center; }
  .phone { font-size: 16px; color: #111; }
  .web { font-size: 11.5px; color: #222; letter-spacing: .3px; }

  .tagline { font-family: "Rubik", sans-serif; font-weight: 400; font-size: 21px; color: #1b1b1b; line-height: 22px; }

  .head { font-family: "Montserrat", sans-serif; font-weight: 700; color: var(--navy); font-size: 19px; line-height: 19px; }
  .body { font-size: 11.5px; line-height: 15px; font-weight: 300; color: #111; }
  .body-light { color: var(--white); }
  .ticks { list-style: none; font-size: 11.5px; line-height: 16.2px; color: #111; }
  .ticks li::before { content: "\2022"; margin-right: 4px; }
  .head-box { background: var(--white); padding: 4px 0 4px 12px; }
  .col { width: 150px; }
</style>
</head>
<body>
<main class="sheet">

  <!-- ===== Outer side ===== -->
  <section class="layer" style="top:0; width:776px; height:600px;">
    <div class="photo" role="img" aria-label="Photo of two people shaking hands across a desk" style="left:0; top:0; width:262px; height:160px; background:linear-gradient(135deg,#e9ecef,#c9d2dc 60%,#dfe3e6);"></div>
    <div class="photo" role="img" aria-label="Photo of a relaxed woman resting on a sofa" style="left:522px; top:120px; width:254px; height:360px; background:linear-gradient(160deg,#f4f1ec,#e6d9cc 45%,#7e9ac6);"></div>

    <svg class="abs" style="left:0; top:0;" width="776" height="600" viewBox="0 0 776 600" aria-hidden="true">
      <path d="M0 205 Q130 150 262 150 L262 495 Q120 482 0 455 Z" fill="var(--slate)"/>
      <path d="M0 172 Q150 118 330 138 Q450 160 522 228 L522 236 Q440 172 330 152 Q150 136 0 208 Z" fill="var(--sky)"/>
      <path d="M0 160 Q160 112 330 132" fill="none" stroke="var(--navy)" stroke-width="6"/>
      <rect x="522" y="420" width="254" height="80" fill="var(--white)"/>
      <path d="M522 120 H776 V330 Q690 430 522 480 Z" fill="none"/>
      <path d="M522 480 Q690 430 776 330 V500 H522 Z" fill="var(--white)"/>
      <path d="M0 455 Q250 522 520 482 Q680 445 776 322 L776 362 Q680 475 520 506 Q250 536 0 472 Z" fill="var(--navy)"/>
      <path d="M280 512 Q600 490 776 372" fill="none" stroke="var(--charcoal)" stroke-width="6"/>
    </svg>

    <div class="fold" style="left:262px; top:0; height:600px;"></div>
    <div class="fold" style="left:522px; top:0; height:600px;"></div>

    <h2 class="about-title abs" style="left:32px; top:222px;">ABOUT US</h2>
    <p class="about-text abs" style="left:32px; top:249px;">We pride ourselves on ours ours delivering elite service, ours great value, honesty and hosty integrity.Lorem ipsum</p>
    <h2 class="why-title abs" style="left:28px; top:328px;">WHY CHOOSE US</h2>
    <ul class="why-dots abs" style="left:34px; top:358px;"><li></li><li></li><li></li><li></li><li></li><li></li></ul>

    <div class="brand abs" style="left:262px; top:52px; width:260px;"><span class="name">PELLOWAY</span><span class="sub">FINANCE</span></div>
    <h2 class="address-title abs" style="left:265px; top:226px;">ADDRESS</h2>
    <div class="photo" role="img" aria-label="Street map showing the office location" style="left:265px; top:253px; width:257px; height:172px; background:linear-gradient(135deg,#b7cdea,var(--map) 55%,#9fc7b4);"></div>
    <p class="phone abs" style="left:327px; top:544px;">PH: (07) 4180 0372</p>
    <p class="web abs" style="left:327px; top:566px;">pellowayfinance.com.au</p>

    <p class="tagline abs" style="left:562px; top:50px; width:200px;">FInance Kept<br><span style="padding-left:110px;">Simple</span></p>
    <div class="brand abs" style="left:522px; top:538px; width:254px;"><span class="name">PELLOWAY</span><span class="sub">FINANCE</span></div>
  </section>

  <!-- ===== Inner side ===== -->
  <section class="layer" style="top:605px; width:776px; height:595px;">
    <div class="abs" style="left:262px; top:10px; width:260px; height:585px; background:var(--pink);"></div>
    <div class="photo" role="img" aria-label="Photo of a surprised woman holding cash and gift boxes" style="left:262px; top:10px; width:260px; height:380px; background:linear-gradient(170deg,var(--pink-soft),#e98fb0 60%,#c9c0c6);"></div>
    <div class="abs" style="left:522px; top:10px; width:254px; height:420px; background:var(--navy);"></div>
    <div class="abs" style="left:522px; top:395px; width:254px; height:200px; background:var(--pink);"></div>
    <div class="photo" role="img" aria-label="Photo of a calculator on printed financial figures" style="left:0; top:420px; width:262px; height:175px; background:linear-gradient(150deg,#5a5f66,#a8acb0 50%,#e6e6e2);"></div>

    <svg class="abs" style="left:0; top:0;" width="776" height="595" viewBox="0 0 776 595" aria-hidden="true">
      <circle cx="720" cy="405" r="45" fill="var(--sky)"/>
      <path d="M0 420 H262 V595 H0 Z" fill="none"/>
      <path d="M0 420 L0 520 Q150 430 262 405 L262 380 H0 Z" fill="var(--white)"/>
      <path d="M0 515 Q250 365 520 378 Q650 386 776 432 L776 448 Q650 405 520 400 Q250 395 0 540 Z" fill="var(--navy)"/>
      <path d="M0 540 Q250 395 520 400 Q650 405 776 448 L776 595 H262 V520 Q120 540 0 560 Z" fill="var(--pink)"/>
      <path d="M0 540 Q140 460 262 430 L262 440 Q140 475 0 555 Z" fill="var(--charcoal)"/>
      <path d="M0 505 Q150 420 262 395" fill="none" stroke="var(--navy)" stroke-width="3"/>
      <rect x="8" y="210" width="190" height="22" fill="var(--navy)"/>
      <circle cx="202" cy="221" r="21" fill="var(--navy)"/>
      <rect x="206" y="215" width="20" height="12" fill="var(--white)"/>
      <rect x="530" y="103" width="100" height="20" fill="var(--charcoal)"/>
      <circle cx="637" cy="113" r="12" fill="var(--sky)"/>
      <rect x="530" y="228" width="128" height="20" fill="var(--charcoal)"/>
      <circle cx="666" cy="238" r="12" fill="var(--sky)"/>
    </svg>

    <div class="fold" style="left:262px; top:10px; height:585px;"></div>
    <div class="fold" style="left:522px; top:10px; height:585px;"></div>

    <h2 class="head abs" style="left:32px; top:43px;">Lorem ipsuorem<br>Ipsum is imply</h2>
    <p class="body abs" style="left:32px; top:88px; width:225px;">Lorem ipsum dolor sit amet, consec-tetuer adipiscing when an unknown printer took a galley of type and scram-bled it to make a type specimen book. It has survived not only five centuries,</p>
    <ul class="ticks abs" style="left:36px; top:245px;">
      <li>We pride ourselves on ours ou</li><li>We pride ourselves on o urs ou</li><li>We pride ourselves on o urs ou</li>
      <li>We pride ourselves on ou rs ou</li><li>We pride ourselves on ou rs ou</li><li>We pride ourselves on ou rs ou</li>
      <li>We pride ourselves on urs ou</li><li>We pride ourselves o ours ou</li><li>We pride ourselves o ours ou</li>
      <li>We pride ourselv on ours ou</li><li>We pes on ours ou</li><li>elves on rs ou</li>
    </ul>

    <div class="head-box abs" style="left:530px; top:38px; width:246px;"><h2 class="head" style="padding-left:22px;">Lorem ipsuLorem<br>Ipsum is simply</h2></div>
    <p class="body body-light abs" style="left:566px; top:136px; width:200px;">Lorem ipsum dolor sit amet, consec-tetuer adipiscing when an unknown printer took a galley of type and scram-bled it to make a type specimen book. It has survived not only five centuries,</p>
    <p class="body body-light abs" style="left:562px; top:257px; width:205px;">Lorem ipsum dolor sit amet, consec-tetuer adipiscing when an unknown printer took a galley of type and scram-bled it to make a type specimen book. It has survived not only five centuries,</p>

    <h2 class="head abs" style="left:299px; top:442px;">Lorem ipsuore Iply</h2>
    <p class="body abs col" style="left:297px; top:490px;">Lorem ipsum dolor sit amet, consectetuer adipiscing when an unknown printer took a galley of type and scram-</p>
    <p class="body abs col" style="left:463px; top:485px;">Lorem ipsum dolor sit amet, consectetuer adipiscing when an unknown printer took a galley of type and scram-</p>
    <p class="body abs col" style="left:623px; top:485px;">Lorem ipsum dolor sit amet, consectetuer adipiscing when an unknown printer took a galley of type and scram-</p>
  </section>

</main>
</body>
</html>
```